Social

We are seeking a skilled designer to create a set of visually compelling social media ad creatives that will drive traffic to our Wood Look Paver landing page, encouraging visitors to download our brochure.
Landing page: https://veltrano.com/wood-look-porcelain-paver-solutions-downloadable-guide/
The broader campaign is focused on educating architects, contractors, and homeowners on the availability and advantages of wood look porcelain pavers as an alternative to natural wood. Ads will highlight both real-world installation images and available wood sample colors to spark interest and drive click-throughs.
Scope:
Design 3 ad sets with distinct styling and copy concepts.
Ads should align with platform best practices for:
Facebook
Instagram
LinkedIn
See brief for sizing.
Creative Direction:
Use installation photos and wood sample color swatches as primary visuals.
Design should clearly highlight the brochure download call-to-action.
Visual style should balance modern and professional, appealing to both design professionals and homeowners.
Target Market(s)
Architects
Industry/Entity Type
Construction
Font styles to use
Other font styles liked:
- Outfit, Helvetica (other fonts are possible)
Look and feel
Each slider illustrates characteristics of the customer's brand and the style your logo design should communicate.

```html
<!DOCTYPE html>
<html lang="en">
<head>
<meta charset="utf-8">
<title>Veltrano – Wood Look Porcelain Pavers Social Ads</title>
<link rel="stylesheet" href="https://fonts.googleapis.com/css2?family=Oswald:wght@600;700&family=Outfit:wght@400&family=Inter:wght@500;600&display=swap">
<style>
  :root {
    --backdrop: #a7a8ac;
    --teal: #0d7d8a;
    --teal-bright: #14a8c2;
    --teal-soft: #8fd3dc;
    --ink: #1d1d1f;
    --white: #ffffff;
    --dark-photo: #2b2623;
  }
  * { box-sizing: border-box; margin: 0; padding: 0; }
  html, body { width: 776px; height: 1200px; overflow: hidden; background: var(--backdrop); }
  .ad {
    position: absolute; left: 94px; width: 588px; height: 308px;
    overflow: hidden; box-shadow: 3px 4px 8px rgba(0,0,0,.35);
    font-family: "Inter", Helvetica, Arial, sans-serif;
  }
  .ad--guide { top: 116px; }
  .ad--sample { top: 446px; background: var(--white); }
  .ad--fireproof { top: 776px; }
  .photo { position: absolute; inset: 0; }
  .brand { position: absolute; display: flex; align-items: center; gap: 8px; }
  .brand__mark { width: 24px; height: 24px; background: var(--teal-bright); }
  .brand__name { font-family: "Outfit", sans-serif; font-weight: 400; font-size: 34px; color: var(--ink); line-height: 1; }
  .headline { position: absolute; left: 30px; font-family: "Oswald", "Arial Narrow", sans-serif; font-weight: 700; text-transform: uppercase; }
  .tagline { position: absolute; left: 32px; font-weight: 600; color: var(--ink); }
  .cta {
    position: absolute; height: 40px; border-radius: 20px;
    background: linear-gradient(#ffffff, #dfe3e4);
    box-shadow: 1px 2px 4px rgba(0,0,0,.35);
    display: flex; align-items: center; justify-content: center; padding-right: 38px;
    font-family: "Oswald", sans-serif; font-weight: 600; font-size: 16px; color: var(--teal);
  }
  .cta__arrow { position: absolute; right: 3px; top: 3px; width: 34px; height: 34px; }
  .swatch { position: absolute; border-radius: 2px; box-shadow: 1px 2px 4px rgba(0,0,0,.4); }
  .tile {
    position: absolute; width: 82px; height: 82px; border-radius: 12px;
    border: 4px solid #f3f3f3; box-shadow: 2px 3px 6px rgba(0,0,0,.4);
  }
  .oak { background: linear-gradient(90deg, #8a7765, #9b8a78 50%, #85715f); }
  .ash { background: linear-gradient(90deg, #c9c9c7, #dededb 50%, #c4c4c1); }
  .cedar { background: linear-gradient(90deg, #9c5a40, #b06c4f 50%, #94553d); }
  .drift { background: linear-gradient(90deg, #8a877f, #aaa69c 50%, #7d7a72); }
</style>
</head>
<body>

<!-- Ad 1: guide download -->
<section class="ad ad--guide">
  <div class="photo" role="img" aria-label="Rooftop terrace with wood look porcelain pavers, lounge seating and glass facade" style="background: linear-gradient(180deg, #4d6f58 0%, #5f8a7c 35%, #2e9aa1 70%, #13848f 100%);"></div>
  <div style="position:absolute;left:380px;top:0;right:0;height:84px;background:var(--white);"></div>
  <div class="brand" style="left:353px;top:26px;">
    <span class="brand__mark"></span><span class="brand__name">Veltrano</span>
  </div>
  <h1 class="headline" style="top:128px;font-size:46px;line-height:44px;color:var(--white);text-shadow:2px 2px 4px rgba(0,0,0,.35);">Wood Look<br>Porcelain Pavers</h1>
  <p class="tagline" style="top:222px;font-size:12.5px;">The warmth of natural wood, the advantages of porcelain.</p>
  <a class="cta" href="https://veltrano.com/wood-look-porcelain-paver-solutions-downloadable-guide/" style="left:31px;top:243px;width:192px;">Download the Guide
    <svg class="cta__arrow" viewBox="0 0 34 34"><circle cx="17" cy="17" r="17" fill="#0d7d8a"/><path d="M14 10l7 7-7 7" fill="none" stroke="#fff" stroke-width="3" stroke-linecap="round" stroke-linejoin="round"/></svg>
  </a>
  <div class="swatch oak" style="left:243px;top:243px;width:39px;height:40px;"></div>
  <div class="swatch ash" style="left:287px;top:243px;width:39px;height:40px;"></div>
  <div class="swatch cedar" style="left:330px;top:243px;width:39px;height:40px;"></div>
  <div class="swatch drift" style="left:374px;top:243px;width:39px;height:40px;"></div>
</section>

<!-- Ad 2: order a sample -->
<section class="ad ad--sample">
  <div class="photo" role="img" aria-label="Terrace with wood look porcelain planks beside a modern glass building and trees" style="left:180px;background: linear-gradient(90deg, rgba(255,255,255,1) 0%, rgba(255,255,255,0) 30%), linear-gradient(180deg, #5d7a64 0%, #6c8a86 40%, #9a8e84 75%, #b3a496 100%);"></div>
  <div class="brand" style="left:30px;top:28px;">
    <span class="brand__mark"></span><span class="brand__name">Veltrano</span>
  </div>
  <h1 class="headline" style="top:92px;font-size:38px;line-height:35px;color:var(--teal);">Wood Look<br>Porcelain<br>Pavers and<br>Planks</h1>
  <p class="tagline" style="top:240px;font-size:13px;line-height:15px;">The rich details of wood,<br>the advantages of porcelain.</p>
  <div style="position:absolute;left:0;top:293px;width:330px;height:15px;background:linear-gradient(90deg,var(--teal),var(--teal-soft) 60%,rgba(143,211,220,0));"></div>
  <div class="tile oak" style="left:255px;top:144px;"></div>
  <div class="tile ash" style="left:323px;top:144px;"></div>
  <div class="tile cedar" style="left:392px;top:144px;"></div>
  <div class="tile drift" style="left:460px;top:144px;"></div>
  <p style="position:absolute;left:259px;top:250px;font-style:italic;color:var(--teal);font-family:Inter,Helvetica,sans-serif;font-weight:600;">
    <span style="font-size:30px;">20+</span><span style="font-size:17px;color:var(--white);"> styles</span>
  </p>
  <a class="cta" href="https://veltrano.com/wood-look-porcelain-paver-solutions-downloadable-guide/" style="left:383px;top:250px;width:164px;">Order a Sample
    <svg class="cta__arrow" viewBox="0 0 34 34"><circle cx="17" cy="17" r="17" fill="#0d7d8a"/><path d="M14 10l7 7-7 7" fill="none" stroke="#fff" stroke-width="3" stroke-linecap="round" stroke-linejoin="round"/></svg>
  </a>
</section>

<!-- Ad 3: fireproof decks -->
<section class="ad ad--fireproof">
  <div class="photo" role="img" aria-label="Covered rooftop terrace with wood look porcelain deck, cafe seating and city view" style="background: linear-gradient(100deg, #2a2522 0%, #3a312b 40%, #6b5a4b 65%, #9aa2a3 100%);"></div>
  <div style="position:absolute;inset:0;background:#0e8a93;clip-path:polygon(220px 308px, 588px 150px, 588px 308px);opacity:.92;"></div>
  <div style="position:absolute;inset:0;background:var(--white);clip-path:polygon(362px 0, 588px 0, 588px 84px, 300px 84px);"></div>
  <div class="brand" style="left:353px;top:26px;">
    <span class="brand__mark"></span><span class="brand__name">Veltrano</span>
  </div>
  <h1 class="headline" style="top:44px;font-size:46px;line-height:44px;color:var(--white);">Build <span style="color:var(--teal-bright);">100%</span><br>Fireproof<br>Decks</h1>
  <p style="position:absolute;left:32px;top:186px;font-size:17px;line-height:19px;font-weight:600;color:var(--teal-bright);">On-grade or elevated<br>on steel pedestals</p>
  <a class="cta" href="https://veltrano.com/wood-look-porcelain-paver-solutions-downloadable-guide/" style="left:31px;top:243px;width:192px;">Learn More
    <svg class="cta__arrow" viewBox="0 0 34 34"><circle cx="17" cy="17" r="17" fill="#0d7d8a"/><path d="M14 10l7 7-7 7" fill="none" stroke="#fff" stroke-width="3" stroke-linecap="round" stroke-linejoin="round"/></svg>
  </a>
  <div class="tile oak" style="left:279px;top:192px;"></div>
  <div class="tile ash" style="left:345px;top:192px;"></div>
  <div class="tile cedar" style="left:411px;top:192px;"></div>
  <div class="tile drift" style="left:477px;top:192px;"></div>
</section>

</body>
</html>
```